Salmon Shop that sells both wholesale and retail salmon in a variety of ways.

"Harbour Fillet Co" is a business that is selling atlantic salmon in every way possible. We will be a salmon butcher to the public for retail purchase and we will also be out and about trying to sell our products to restaurants cafes and any other wholesale way. Our product is from Tasmania but we will be trading on the Sunshine Coast. The shop design has an urban, rustic feel and very much about the product. One of the owners has worked on salmon farms for 15 years and we want it to be very specialised and quality. I have nothing to offer you to help with this design....I would like both a salmon on the card, not sure if image or silohette is best and would like the other side to have a fillet with a tag of some sort. We are looking for a logo also. Use a photo of an Atlantic Salmon, Atlantic Salmon have two fins along the back.
Updates

Project Deadline Extended Reason: I am extending the deadline as I have still not got exactly what I want. All designers have added something great to what I am after and I just need someone to pull it all together. I have put in a new brief with a sketched image to help so we can get this perfect. Please read all the instructions. Thank you Added Monday, February 16, 2015

Target Market(s)

Restaurants, cafes

Industry/Entity Type

Retail

Contact Information for Business Card

Harbour Fillet Co (Not to have "Shop" at the end.Shop 12/130-164 Brisbane RdMooloolaba 4557

Colors
1c66ab

Requirements
Must have
• logo for harbour fillet Co with the S being salmon fillet of fresh salmon on white platemap of tasmaniasepia /black and white image of atlantic salmon
Nice to have
• fillet of salmonmap of tasmaniasalmon
Should not have
• Not Shop at the end.

```html
<!DOCTYPE html>
<html lang="en">
<head>
<meta charset="utf-8">
<title>Harbour Fillet Co – Business Card</title>
<link rel="stylesheet" href="https://fonts.googleapis.com/css2?family=Poppins:wght@600&family=Open+Sans:wght@400&display=swap">
<style>
  :root {
    --backdrop: #d1d1d1;
    --card: #ffffff;
    --brand-green: #149a7a;
    --ink: #1e1e1e;
    --photo-warm: #e08a4e;
    --photo-light: #f3d3b6;
    --card-shadow: rgba(0, 0, 0, 0.28);
  }
  * { box-sizing: border-box; margin: 0; padding: 0; }
  html, body {
    width: 1200px;
    height: 800px;
    overflow: hidden;
    background: var(--backdrop);
  }
  .canvas {
    position: relative;
    width: 1200px;
    height: 800px;
    display: flex;
    align-items: center;
    justify-content: space-evenly;
  }
  .card {
    position: relative;
    width: 520px;
    height: 297px;
    background: var(--card);
    overflow: hidden;
    box-shadow: 2px 3px 6px var(--card-shadow);
  }
  .brand-name {
    font-family: "Poppins", sans-serif;
    font-weight: 600;
    color: var(--brand-green);
    font-size: 34px;
    line-height: 1;
    letter-spacing: 0.5px;
    white-space: nowrap;
  }
  .brand-lockup {
    display: flex;
    align-items: center;
    gap: 12px;
  }
  .brand-dot {
    width: 18px;
    height: 18px;
    border-radius: 50%;
    background: var(--brand-green);
    flex: none;
  }

  /* Front: contact side */
  .card--contact .corner-stripes {
    position: absolute;
    left: 0;
    top: 0;
    width: 150px;
    height: 150px;
  }
  .card--contact .brand-lockup {
    position: absolute;
    left: 118px;
    top: 86px;
  }
  .contact-details {
    position: absolute;
    left: 118px;
    top: 168px;
    font-family: "Open Sans", sans-serif;
    font-style: normal;
    font-size: 17px;
    line-height: 1.55;
    color: var(--ink);
  }

  /* Back: photo side */
  .card--photo .photo-area {
    position: absolute;
    left: 0;
    top: 0;
    width: 520px;
    height: 297px;
  }
  .card--photo .brand-lockup {
    position: absolute;
    right: 30px;
    bottom: 30px;
  }
</style>
</head>
<body>
<main class="canvas">

  <section class="card card--contact" aria-label="Business card, contact side">
    <svg class="corner-stripes" viewBox="0 0 150 150" aria-hidden="true">
      <polygon points="42,0 60,0 0,60 0,42" fill="var(--brand-green)"/>
      <polygon points="92,0 110,0 0,110 0,92" fill="var(--brand-green)"/>
    </svg>
    <div class="brand-lockup">
      <span class="brand-dot"></span>
      <span class="brand-name">Harbour Fillet Co</span>
    </div>
    <address class="contact-details">
      <p>7/210-236 Wattlebay Rd Kirrawee 4812</p>
      <p>Call:-0000-000-000</p>
    </address>
  </section>

  <section class="card card--photo" aria-label="Business card, photo side">
    <svg class="photo-area" viewBox="0 0 520 297">
      <defs>
        <linearGradient id="filletTone" x1="0" y1="0" x2="1" y2="1">
          <stop offset="0" stop-color="var(--photo-light)"/>
          <stop offset="0.45" stop-color="var(--photo-warm)"/>
          <stop offset="1" stop-color="var(--photo-light)"/>
        </linearGradient>
      </defs>
      <circle cx="140" cy="15" r="185" fill="var(--brand-green)"/>
      <circle cx="140" cy="15" r="168" fill="url(#filletTone)"
              role="img" aria-label="Photo of a sesame-crusted salmon fillet on sliced red onion with lettuce"/>
    </svg>
    <div class="brand-lockup">
      <span class="brand-dot"></span>
      <span class="brand-name">Harbour Fillet Co</span>
    </div>
  </section>

</main>
</body>
</html>
```